1912 Zur Glutpfanne Website
Zielgruppe
Wir betreiben ein Hamburger-Restaurant. Alle Zutaten kommen wenn möglich, aus der Region. Wir benutzen keine Farb- und Konservierungsstoffe. Unser Fleisch ist ein frisches Bio-Rinderhack. Das Brot backen wir selber und die Saucen sind nach eigener Rezeptur hausgemacht. Der Käse wird in einem Familienbetrieb frisch für uns hergestellt. Jeder Gast kann sich seinen Burger frisch nach seinen Wünschen zusammenstellen und bei der Zubereitung zuschauen. Essen mit Herkunft aus Tradition!
Aufgabenstellung
Ansprechendes Design, welches unsere Philosophie und die Liebe zum Burger widerspiegelt. Frische Zutaten in wechselnden Slide-Shows, Wertschätzung der Rohprodukte und den Genuss beim Essen.

```html
<!DOCTYPE html>
<html lang="de">
<head>
<meta charset="utf-8">
<title>1912 Zur Glutpfanne</title>
<link rel="stylesheet" href="https://fonts.googleapis.com/css2?family=Lobster&family=Lobster+Two:ital,wght@1,700&family=Signika:wght@600&family=Open+Sans:wght@600&display=swap">
<style>
:root{
  --orange-top:#ffb96a;
  --orange-bottom:#f39a45;
  --red:#d5331c;
  --brown:#4a2410;
  --brown-dark:#3b1d0c;
  --footer:#7a4030;
  --gold:#c9984a;
  --green:#8dc63f;
  --green-dark:#6fa72a;
  --paper:#efeae3;
  --white:#ffffff;
  --rule:#e4ded3;
  --link:#3b6ea8;
}
*{margin:0;padding:0;box-sizing:border-box}
html,body{width:1200px;height:2500px;overflow:hidden}
body{position:relative;background:var(--paper);font-family:'Signika',sans-serif;color:var(--brown)}

.site-header{position:absolute;left:0;top:0;width:1200px;height:124px;background:linear-gradient(var(--orange-top),var(--orange-bottom));border-bottom:11px solid var(--red);z-index:2}
.main-nav a,.footer-nav a{position:absolute;text-decoration:none;font-family:'Signika',sans-serif;font-weight:600;letter-spacing:.6px}
.main-nav a{top:50px;font-size:17px;color:var(--brown)}

.brand{position:absolute;border-radius:50%;background:var(--brown-dark);display:flex;align-items:center;justify-content:center;text-align:center;color:var(--white);font-family:'Lobster',cursive;line-height:1.05;z-index:5}
.brand-top{left:133px;top:38px;width:148px;height:148px;font-size:24px}
.brand-foot{left:130px;top:2270px;width:128px;height:128px;font-size:21px}

.hero{position:absolute;left:0;top:124px;width:1200px;height:515px;overflow:hidden;
  background:
    radial-gradient(ellipse 230px 90px at 860px 230px,rgba(236,40,24,.85),transparent 70%),
    radial-gradient(ellipse 300px 110px at 800px 160px,rgba(250,205,80,.9),transparent 70%),
    radial-gradient(ellipse 330px 90px at 850px 320px,rgba(70,35,20,.95),transparent 72%),
    radial-gradient(ellipse 360px 120px at 880px 430px,rgba(226,170,90,.95),transparent 70%),
    radial-gradient(ellipse 200px 90px at 820px 40px,rgba(168,78,28,.9),transparent 70%),
    radial-gradient(ellipse 260px 140px at 260px 60px,rgba(175,110,55,.85),transparent 70%),
    radial-gradient(ellipse 180px 240px at 90px 300px,rgba(220,180,135,.9),transparent 72%),
    radial-gradient(ellipse 240px 160px at 330px 420px,rgba(240,180,70,.95),transparent 70%),
    radial-gradient(ellipse 180px 200px at 540px 260px,rgba(110,165,50,.55),transparent 70%),
    linear-gradient(135deg,#4a2c1c,#2e1b12 60%,#3b2417)}
.hero-caption{position:absolute;background:rgba(141,198,63,.93);color:var(--white);font-family:'Lobster',cursive;text-shadow:1px 2px 2px rgba(0,0,0,.35);padding-left:32px;display:flex;align-items:center;font-size:42px}
.hero-arrow{position:absolute;top:244px;width:54px;height:54px}
.dot{position:absolute;top:453px;width:15px;height:15px;border-radius:50%;background:var(--white)}
.dot.active{background:var(--green);border:2px solid var(--white)}

.intro{position:absolute;left:0;top:639px;width:1200px;height:203px;background:var(--white);border-bottom:1px solid var(--rule)}
.intro h1{position:absolute;left:290px;top:74px;width:620px;text-align:center;font-family:'Lobster Two',cursive;font-style:italic;font-weight:700;font-size:31px;line-height:36px;letter-spacing:2px;text-transform:uppercase;color:var(--brown-dark)}
.chev{position:absolute;top:96px}

.news{position:absolute;left:131px;top:842px;width:936px;height:1023px;background:var(--white)}
.news-item{position:absolute;left:0;width:936px}
.news-photo{position:absolute;left:15px;top:0;width:305px;height:203px}
.photo-fries{background:
  radial-gradient(ellipse 110px 60px at 140px 130px,rgba(246,196,70,.95),transparent 72%),
  radial-gradient(ellipse 70px 40px at 220px 140px,rgba(190,60,35,.85),transparent 72%),
  radial-gradient(ellipse 40px 50px at 285px 30px,rgba(200,40,35,.8),transparent 70%),
  linear-gradient(180deg,#c4c8cc,#e9e9e6 60%,#cfcfcc)}
.photo-grill{background:
  radial-gradient(ellipse 60px 35px at 150px 50px,rgba(150,90,70,.95),transparent 72%),
  radial-gradient(ellipse 80px 45px at 120px 105px,rgba(140,85,65,.95),transparent 72%),
  radial-gradient(ellipse 55px 35px at 230px 85px,rgba(130,80,60,.95),transparent 72%),
  radial-gradient(ellipse 60px 40px at 215px 145px,rgba(120,70,55,.95),transparent 72%),
  radial-gradient(ellipse 200px 100px at 240px 200px,rgba(245,140,40,.9),transparent 75%),
  linear-gradient(135deg,#1e1410,#3a1f14 50%,#d96a22)}
.photo-plate{background:
  radial-gradient(ellipse 80px 30px at 110px 25px,rgba(214,150,70,1),transparent 72%),
  radial-gradient(ellipse 90px 22px at 95px 75px,rgba(60,35,25,1),transparent 72%),
  radial-gradient(ellipse 80px 20px at 95px 105px,rgba(220,80,60,.9),transparent 72%),
  radial-gradient(ellipse 120px 70px at 220px 150px,rgba(236,190,90,.95),transparent 72%),
  linear-gradient(160deg,#e9e3d8,#f3efe8 50%,#d6cfc2)}
.news-title{position:absolute;left:352px;font-family:'Lobster',cursive;font-size:30px;color:var(--gold);font-weight:400;white-space:nowrap}
.news-text{position:absolute;left:352px;width:392px;font-family:'Lobster Two',cursive;font-style:italic;font-weight:700;font-size:14px;line-height:17px;letter-spacing:.35px;color:var(--brown-dark)}
.btn-more{position:absolute;left:352px;width:92px;height:32px;border-radius:4px;background:linear-gradient(var(--green),var(--green-dark));color:var(--white);font-family:'Lobster Two',cursive;font-style:italic;font-weight:700;font-size:13px;display:flex;align-items:center;justify-content:center;text-decoration:none}
.news-rule{position:absolute;left:24px;width:897px;height:1px;background:var(--rule)}

.pager{position:absolute;top:943px;width:33px;height:32px;display:flex;align-items:center;justify-content:center;font-family:'Open Sans',sans-serif;font-size:13px;color:#555;background:#efece6;text-decoration:none}
.pager.nav{background:var(--red);color:var(--white);font-size:18px}
.badge{position:absolute;left:770px;top:856px}

.social{position:absolute;left:130px;top:1970px;width:468px;height:258px;background:var(--white);box-shadow:0 1px 3px rgba(0,0,0,.08)}
.social-fold{position:absolute;right:0;top:0}
.social-mark{position:absolute;left:24px;top:34px;width:45px;height:44px;background:#3b5a98;border-radius:3px}
.social-name{position:absolute;left:93px;top:42px;font-family:'Lobster Two',cursive;font-style:italic;font-weight:700;font-size:17px;color:var(--brown-dark)}
.social-rule{position:absolute;left:93px;top:71px;width:306px;height:1px;background:#ccc}
.social-stats,.social-post{position:absolute;left:95px;width:330px;font-family:Arial,sans-serif;font-style:italic;font-size:13.5px;line-height:17px;color:var(--link);letter-spacing:.3px}
.social-stats{top:98px}
.social-post{top:132px;text-decoration:underline}
.like-btn{position:absolute;left:98px;top:218px;width:40px;height:17px;background:#5471b0;border-radius:2px}
.like-count{position:absolute;left:141px;top:218px;width:24px;height:17px;border:1px solid #aaa;background:var(--white)}

.lettuce{position:absolute;left:880px;top:1960px;width:280px;height:260px;
  background:
    radial-gradient(ellipse 70px 90px at 150px 90px,rgba(190,230,110,.9),transparent 70%),
    radial-gradient(ellipse 120px 120px at 140px 130px,rgba(110,175,45,.95),transparent 72%),
    radial-gradient(ellipse 140px 130px at 140px 130px,rgba(60,120,30,.5),transparent 75%)}

.site-footer{position:absolute;left:0;top:2323px;width:1200px;height:177px;background:var(--footer)}
.footer-nav a{top:45px;font-size:17px;color:var(--white)}
.copyright{position:absolute;left:0;top:122px;width:1115px;text-align:center;font-family:'Open Sans',sans-serif;font-weight:600;font-size:11px;color:var(--white)}
</style>
</head>
<body>

<header class="site-header">
  <nav class="main-nav">
    <a href="#" style="left:488px">Home</a>
    <a href="#" style="left:596px">Unser Restaurant</a>
    <a href="#" style="left:812px">Reservierungen</a>
    <a href="#" style="left:1002px">Kontakt</a>
  </nav>
</header>
<div class="brand brand-top">1912<br>Zur<br>Glutpfanne</div>

<section class="hero" role="img" aria-label="Foto: gegrillter Burger mit Käse, Tomate und Zwiebelringen neben Pommes in einer Papiertüte auf Holz">
  <div class="hero-caption" style="left:624px;top:116px;width:435px;height:68px">Spicy Grilled Burger</div>
  <div class="hero-caption" style="left:65px;top:363px;width:435px;height:68px">Tasty crispy fries</div>
  <svg class="hero-arrow" style="left:58px" viewBox="0 0 54 54"><circle cx="27" cy="27" r="27" fill="#d5331c"/><path d="M31 16 L20 27 L31 38" fill="none" stroke="#fff" stroke-width="4" stroke-linecap="round"/></svg>
  <svg class="hero-arrow" style="left:1081px" viewBox="0 0 54 54"><circle cx="27" cy="27" r="27" fill="#d5331c"/><path d="M23 16 L34 27 L23 38" fill="none" stroke="#fff" stroke-width="4" stroke-linecap="round"/></svg>
  <span class="dot active" style="left:543px;top:451px;width:19px;height:19px"></span>
  <span class="dot" style="left:578px"></span>
  <span class="dot" style="left:603px"></span>
  <span class="dot" style="left:629px"></span>
</section>

<section class="intro">
  <svg class="chev" style="left:131px" width="28" height="36" viewBox="0 0 28 36"><path d="M22 2 L6 18 L22 34" fill="none" stroke="#3b1d0c" stroke-width="5"/></svg>
  <h1>Das Fast-Food-Urgestein findet seine Wurzeln</h1>
  <svg class="chev" style="left:1040px" width="28" height="36" viewBox="0 0 28 36"><path d="M6 2 L22 18 L6 34" fill="none" stroke="#3b1d0c" stroke-width="5"/></svg>
</section>

<main class="news">
  <article class="news-item" style="top:68px">
    <div class="news-photo photo-fries" role="img" aria-label="Foto: Pommes frites mit Currywurst in einer Papierschale"></div>
    <h2 class="news-title" style="top:5px">Tasty crispy fries</h2>
    <p class="news-text" style="top:57px">Lorem ipsum magna aliquam erat volutpat. Ut wisi enim ad minim veniam, quis nostrud exerci tation ullamcorper suscipit lobortis nisl ut aliquip ex ea commodo consequat.</p>
    <a class="btn-more" href="#" style="top:123px">Read more</a>
  </article>
  <div class="news-rule" style="top:327px"></div>

  <article class="news-item" style="top:381px">
    <div class="news-photo photo-grill" role="img" aria-label="Foto: Burger-Patties auf einem Grillrost über Flammen"></div>
    <h2 class="news-title" style="top:23px">Tasty crispy fries</h2>
    <p class="news-text" style="top:75px">Lorem ipsum magna aliquam erat volutpat. Ut wisi enim ad minim veniam, quis nostrud exerci tation ullamcorper suscipit lobortis nisl ut aliquip ex ea commodo consequat.</p>
    <a class="btn-more" href="#" style="top:141px">Read more</a>
  </article>
  <div class="news-rule" style="top:638px"></div>

  <article class="news-item" style="top:690px">
    <div class="news-photo photo-plate" role="img" aria-label="Foto: Burger mit Pommes frites auf einem Teller" style="left:13px;width:306px"></div>
    <h2 class="news-title" style="top:23px">Tasty crispy fries</h2>
    <p class="news-text" style="top:75px">Lorem ipsum magna aliquam erat volutpat. Ut wisi enim ad minim veniam, quis nostrud exerci tation ullamcorper suscipit lobortis nisl ut aliquip ex ea commodo consequat.</p>
    <a class="btn-more" href="#" style="top:141px">Read more</a>
  </article>

  <a class="pager nav" href="#" style="left:362px">&lsaquo;&lsaquo;</a>
  <a class="pager" href="#" style="left:407px">1</a>
  <a class="pager" href="#" style="left:452px">2</a>
  <a class="pager" href="#" style="left:497px">3</a>
  <a class="pager nav" href="#" style="left:541px">&rsaquo;&rsaquo;</a>

  <svg class="badge" width="135" height="135" viewBox="0 0 135 135">
    <polygon fill="#8dc63f" points="67.5,0 74,12 84,3 87,16 99,10 98,23 111,21 106,33 119,35 111,45 123,51 112,58 122,67 111,73 119,83 106,86 111,98 98,97 100,110 87,105 85,118 75,109 67.5,121 60,109 50,118 48,105 35,110 37,97 24,98 29,86 16,83 24,73 13,67 23,58 12,51 24,45 16,35 29,33 24,21 37,23 36,10 48,16 51,3 61,12"/>
    <text x="66" y="60" text-anchor="middle" transform="rotate(-18 66 60)" font-family="Lobster Two, cursive" font-style="italic" font-weight="700" font-size="22" fill="#fff">100%</text>
    <text x="70" y="85" text-anchor="middle" transform="rotate(-18 70 85)" font-family="Lobster Two, cursive" font-style="italic" font-weight="700" font-size="20" fill="#fff">reines</text>
  </svg>
</main>

<aside class="social">
  <svg class="social-fold" width="40" height="34" viewBox="0 0 40 34"><polygon points="0,0 40,34 40,0" fill="#efeae3"/><polygon points="0,0 40,34 8,30" fill="#e6dfcf"/></svg>
  <span class="social-mark"></span>
  <div class="social-name">Zur Glutpfanne</div>
  <div class="social-rule"></div>
  <p class="social-stats">651856 Fans · 3269 sprechen darüber</p>
  <p class="social-post">Morgen ist es soweit. Die KNUSPERSTICKS™ sind in deiner Stadt! Am 15. und 16. März kannst du eine kleine Portion gratis bei deinem Zur Glutpfanne</p>
  <span class="like-btn"></span>
  <span class="like-count"></span>
</aside>

<div class="lettuce" role="img" aria-label="Foto: frischer grüner Salatkopf"></div>

<footer class="site-footer">
  <nav class="footer-nav">
    <a href="#" style="left:309px">Home</a>
    <a href="#" style="left:417px">Unser Restaurant</a>
    <a href="#" style="left:633px">Reservierungen</a>
    <a href="#" style="left:822px">Kontakt</a>
  </nav>
  <p class="copyright">Copyright © 2014 All rights reserved.</p>
</footer>
<div class="brand brand-foot">1912<br>Zur<br>Glutpfanne</div>

</body>
</html>
```